Bright Fern Landscape Services LLC
business cards, letterhead, and envelopes.
Bright Fern Landscape Services LLC -
Creative Brief
Simple
Lydia Harcourt
Owner
2187 NW 58th Ave. Ocala, Fl 34475
lharcourt@quillmesh.net
Would like to use my tagline somewhere not necessarily right under the logo.

```html
<!DOCTYPE html>
<html lang="en">
<head>
<meta charset="utf-8">
<title>Bright Fern Landscape Services LLC – Business Card</title>
<link rel="stylesheet" href="https://fonts.googleapis.com/css2?family=Open+Sans:wght@400;600;700;800&display=swap">
<style>
  :root {
    --bg: #e9eae7;
    --card: #ffffff;
    --green: #3f9b1e;
    --green-light: #7cc242;
    --orange: #f0801f;
    --ink: #4a4a4a;
    --rule: #b9b9b9;
  }
  * { margin: 0; padding: 0; box-sizing: border-box; }
  html, body {
    width: 1200px; height: 799px; overflow: hidden;
    background: var(--bg);
    font-family: "Open Sans", Arial, sans-serif;
  }
  .stage { position: relative; width: 1200px; height: 799px; }
  .card {
    position: absolute; top: 255px;
    width: 500px; height: 290px;
    background: var(--card);
    border-radius: 16px;
    overflow: hidden;
    box-shadow: 0 6px 18px rgba(0,0,0,0.12);
  }
  .card--front { left: 70px; }
  .card--back { left: 630px; }

  .brand { display: flex; align-items: center; gap: 10px; }
  .brand__dot {
    width: 22px; height: 22px; border-radius: 50%;
    background: var(--orange); flex: none;
  }
  .brand__name {
    font-weight: 800; color: var(--green);
    font-size: 19px; line-height: 1.2; white-space: nowrap;
  }
  .card--front .brand { position: absolute; left: 26px; top: 72px; }
  .card--back .brand {
    position: absolute; left: 0; right: 0; top: 112px;
    justify-content: center;
  }
  .card--back .brand__name { font-size: 22px; }

  .divider {
    position: absolute; left: 292px; top: 50px;
    width: 1px; height: 150px; background: var(--rule);
  }
  .contact {
    position: absolute; left: 306px; top: 58px;
    list-style: none; font-size: 11px; color: var(--ink);
  }
  .contact li {
    display: flex; align-items: flex-start; gap: 7px; margin-bottom: 10px; line-height: 1.35;
  }
  .contact svg { flex: none; margin-top: 1px; }

  .person { position: absolute; left: 30px; top: 178px; }
  .person__name { font-weight: 700; font-size: 15px; color: var(--green); }
  .person__title {
    font-weight: 600; font-size: 11px; color: var(--orange);
    text-align: right; margin-top: 1px;
  }
  .swoosh { position: absolute; left: 0; bottom: 0; width: 500px; height: 90px; }
</style>
</head>
<body>
<main class="stage">
  <section class="card card--front" aria-label="Business card front">
    <div class="brand">
      <span class="brand__dot"></span>
      <span class="brand__name">Bright Fern<br>Landscape Services LLC</span>
    </div>

    <div class="divider"></div>

    <ul class="contact">
      <li>
        <svg width="11" height="13" viewBox="0 0 11 13"><path d="M5.5 0C2.5 0 0.5 2.2 0.5 4.8c0 3.4 5 8.2 5 8.2s5-4.8 5-8.2C10.5 2.2 8.5 0 5.5 0z" fill="var(--green)"/><circle cx="5.5" cy="4.8" r="1.8" fill="#fff"/></svg>
        <span>2187 NW 58th Ave.<br>Ocala, Fl 34475</span>
      </li>
      <li>
        <svg width="11" height="12" viewBox="0 0 11 12"><path d="M2.4 0.5l2 2.6-1.2 1.5c0.7 1.6 1.9 2.9 3.4 3.7l1.5-1.2 2.4 2-1.2 2.4C5 11 0.5 6.5 0.2 1.8z" fill="var(--green)"/></svg>
        <span>(555) 014-7203</span>
      </li>
      <li>
        <svg width="12" height="12" viewBox="0 0 12 12"><circle cx="6" cy="6" r="6" fill="var(--green)"/><rect x="3" y="4" width="6" height="4.2" fill="#fff"/><path d="M3 4l3 2.3L9 4" stroke="var(--green)" stroke-width="0.8" fill="none"/></svg>
        <span>lharcourt@quillmesh.net</span>
      </li>
    </ul>

    <div class="person">
      <p class="person__name">Lydia Harcourt</p>
      <p class="person__title">Owner</p>
    </div>

    <svg class="swoosh" viewBox="0 0 500 90" preserveAspectRatio="none" aria-hidden="true">
      <defs>
        <linearGradient id="greenBand" x1="0" y1="0" x2="1" y2="0">
          <stop offset="0" stop-color="#3f9b1e"/>
          <stop offset="1" stop-color="#7cc242"/>
        </linearGradient>
      </defs>
      <path d="M0 62 C150 80 330 40 500 14 L500 90 L0 90 Z" fill="url(#greenBand)"/>
      <path d="M0 56 C150 74 330 34 500 6" stroke="#f0801f" stroke-width="3" fill="none"/>
    </svg>
  </section>

  <section class="card card--back" aria-label="Business card back">
    <div class="brand">
      <span class="brand__dot"></span>
      <span class="brand__name">Bright Fern<br>Landscape Services LLC</span>
    </div>
  </section>
</main>
</body>
</html>
```